Breezy Burro Menu Design for new restaurant

Need a menu design for new restaurant- Fast Casual Taqueria. I have the files for our logo and menu already completed. Let me know what type of file your require and I can send it with regard to my logo. I want it to be easy to read but on a half page rack size type card, front and back. Simple and to the point but important to include the items listed with ingredients. Feel free to use icons for different categories.

Target Market(s)

Any one who loves tacos and margaritas...fun...festive...casual...

Font styles to use
Other font styles liked:
• lobster 1.3 and farmer round

Colors
3276b5
ec1f27
ffffff
85cae6
9bcb3c
fbed22

Requirements
Must have
• Designed for a half page, front and back (4.25 x 11). NO full size page menu. Easy to read. Not complicated. Use our logo. I need to be able to modify the menu from my end with out any special software.
Nice to have
• Fun~Festive~ color. Stick with our logo theme using our font lobster 1.3 and farmer round.
Should not have
• Full page format. Do not want stock food phots. Just graphics or icons.

```html
<!DOCTYPE html>
<html lang="en">
<head>
<meta charset="utf-8">
<title>Breezy Burro Menu</title>
<link rel="stylesheet" href="https://fonts.googleapis.com/css2?family=Lobster&family=Oswald:wght@400;500&display=swap">
<style>
  :root {
    --ink-blue: #2d62a8;
    --sky: #85cae6;
    --red: #f1414a;
    --brand-red: #ec1f27;
    --white: #ffffff;
    --yellow: #fbed22;
    --backdrop: #e4e4e4;
    --cream: #f3e9d6;
    --sepia: #c9a98a;
  }
  * { box-sizing: border-box; margin: 0; padding: 0; }
  html, body { width: 1200px; height: 1200px; overflow: hidden; }
  body { background: var(--backdrop); position: relative; font-family: "Oswald", sans-serif; }

  .menu-card { position: absolute; background: var(--white); box-shadow: 0 10px 24px rgba(0,0,0,.18); }
  .menu-card--front { left: 116px; top: 90px; width: 458px; height: 954px; }
  .menu-card--back { left: 630px; top: 146px; width: 452px; height: 944px; }

  .brand-name {
    position: absolute; left: 0; right: 0; text-align: center;
    font-family: "Lobster", cursive; font-size: 36px; color: var(--brand-red);
    display: flex; align-items: center; justify-content: center; gap: 8px;
  }
  .brand-dot { width: 12px; height: 12px; border-radius: 50%; background: var(--sky); }
  .menu-card--front .brand-name { top: 40px; }
  .menu-card--back .brand-name { top: 38px; }

  .panel { position: absolute; }
  .panel--sky { background: var(--sky); }
  .panel--red { background: var(--red); }
  .panel--yellow { background: var(--yellow); }

  .bubble { position: absolute; border-radius: 50%; background: var(--white); }

  .menu-list { position: absolute; list-style: none; display: flex; flex-direction: column; }
  .menu-item h3 { font-family: "Lobster", cursive; font-weight: 400; font-size: 21px; line-height: 1.05; }
  .menu-item p { font-size: 9px; line-height: 1.2; text-transform: uppercase; letter-spacing: .1px; }
  .panel--sky .menu-item h3, .panel--sky .menu-item p { color: var(--ink-blue); }
  .panel--red .menu-item h3, .panel--red .menu-item p { color: var(--white); }

  .menu-list--starters p { max-width: 272px; }
  .menu-list--tacos p { max-width: 232px; }
  .menu-list--signature p { max-width: 300px; }
  .menu-list--bowls p { max-width: 248px; }

  .section-tab {
    position: absolute; left: 0; background: var(--white);
    font-family: "Lobster", cursive; line-height: 1;
  }
  .section-tab--tacos { top: 5px; font-size: 32px; color: var(--red); padding: 8px 22px 8px 30px; border-radius: 0 30px 30px 0; }
  .section-tab--bowl { top: 8px; font-size: 22px; color: var(--ink-blue); padding: 6px 10px 6px 24px; border-radius: 0 30px 30px 0; }
  .section-tab--drink { right: 0; left: auto; top: 12px; font-size: 22px; color: var(--ink-blue); padding: 4px 28px 4px 18px; border-radius: 30px 0 0 30px; }

  .section-note { position: absolute; color: var(--white); text-transform: uppercase; }
  .section-note--tacos { left: 33px; top: 64px; font-size: 14px; line-height: 1.15; width: 300px; }
  .section-note--bowl { right: 74px; top: 46px; font-size: 10.5px; font-style: italic; }

  .drink-list { position: absolute; left: 40px; top: 10px; list-style: none; }
  .drink-list li { font-size: 9px; line-height: 13.1px; color: var(--ink-blue); text-transform: uppercase; display: flex; }
  .drink-list .col-a { width: 118px; }
  .drink-list .col-a--wide { width: 160px; }
  .drink-list .col-b { width: 80px; }

  .illustration { position: absolute; border-radius: 12px; background: linear-gradient(160deg, var(--cream), var(--sepia)); opacity: .9; }
</style>
</head>
<body>

<section class="menu-card menu-card--front">
  <div class="brand-name"><span class="brand-dot"></span>Breezy Burro</div>

  <div class="panel panel--sky" style="left:18px;top:124px;width:421px;height:492px;">
    <span class="bubble" style="left:328px;top:-6px;width:32px;height:32px;"></span>
    <span class="bubble" style="left:366px;top:14px;width:18px;height:18px;"></span>
    <ul class="menu-list menu-list--starters" style="left:38px;top:8px;gap:9px;">
      <li class="menu-item"><h3>Mexican Poke</h3><p>Fresh ahi tuna blended w/ spices &amp; ponzu on a bed of colored cabbage</p></li>
      <li class="menu-item"><h3>Mermaid Tails</h3><p>Shrimp tempura beached on coconut slaw w/ sweet heat glaze, rice pearls, fresh cilantro</p></li>
      <li class="menu-item"><h3>Fiesta Nachos</h3><p>Crunchy tortilla chips layered w/ queso fresco, pickled vegetables, black beans, tomatillo salsa, dry chile salsa &amp; cilantro. As flavorful as it is colorful!</p></li>
      <li class="menu-item"><h3>Chorizo &amp; Questo</h3><p>Melted queso fresco w/ chorizo crumbles, caramelized onions, cilantro</p></li>
      <li class="menu-item"><h3>Elote</h3><p>Roasted corn sliced from the cob, chopped onions and poblano peppers w/ cotija cheese, smoky homemade morita mayo &amp; Diablita</p></li>
      <li class="menu-item"><h3>Guacamole &amp; Chips</h3><p>Smooth blend of Haas avocados, jalapeño, red onions</p></li>
      <li class="menu-item"><h3>Chips and Salsa</h3><p>Tortilla chips w/ choice of traditional rojo salsa or tomatillo verde</p></li>
      <li class="menu-item"><h3>Queso and Chips</h3><p>Melted queso fresco &amp; crunchy tortilla chips</p></li>
      <li class="menu-item"><h3>Rice &amp; Black Beans</h3><p>Traditional Mexican arroz verde &amp; black beans seasoned w/ epazote</p></li>
    </ul>
  </div>
  <div class="illustration" role="img" aria-label="Sketch of french fries in a paper carton" style="left:354px;top:506px;width:92px;height:136px;"></div>

  <div class="panel panel--red" style="left:18px;top:636px;width:421px;height:302px;">
    <div class="section-tab section-tab--tacos">Tacos</div>
    <span class="bubble" style="left:376px;top:16px;width:32px;height:32px;"></span>
    <span class="bubble" style="left:358px;top:52px;width:18px;height:18px;"></span>
    <p class="section-note section-note--tacos">All tacos finished Breezy style with fresh cilantro, side of dry chile salsa &amp; lime wedges</p>
    <ul class="menu-list menu-list--tacos" style="left:42px;top:112px;gap:18px;">
      <li class="menu-item"><h3>Korean</h3><p>Braised short ribs, caramelized onions, cucumber salad, gochujang sauce</p></li>
      <li class="menu-item"><h3>Barbacoa</h3><p>Spiced angus beef, cool creama, white diced onion, tomatillo-avocado salsa</p></li>
      <li class="menu-item"><h3>Al Pastor</h3><p>Spit-grilled heritage pork, diced white onion, charred pineapple, queso fresco</p></li>
    </ul>
  </div>
  <div class="illustration" role="img" aria-label="Sketch of a taco with radiating lines" style="left:312px;top:808px;width:140px;height:140px;"></div>
</section>

<section class="menu-card menu-card--back">
  <div class="brand-name"><span class="brand-dot"></span>Breezy Burro</div>

  <div class="panel panel--red" style="left:16px;top:116px;width:420px;height:472px;">
    <span class="bubble" style="left:328px;top:-4px;width:32px;height:32px;"></span>
    <span class="bubble" style="left:366px;top:18px;width:18px;height:18px;"></span>
    <ul class="menu-list menu-list--signature" style="left:41px;top:10px;gap:10px;">
      <li class="menu-item"><h3>Carnitas</h3><p>Slow simmered heritage pork, avocado smash, pickled red onion, blistered shishito peppers</p></li>
      <li class="menu-item"><h3>Alabama Slamma</h3><p>Pulled smoked chicken, Alabama white sauce, pickled cabbage, fried onions, bacon blanket</p></li>
      <li class="menu-item"><h3>Chick Next Door</h3><p>Grilled chicken breast, elote, avocado smash, queso fresco, salsa verde</p></li>
      <li class="menu-item"><h3>Yinzer</h3><p>Grilled flat iron steak w/peppers &amp; onions, melted queso fresco, house jalapeño salsa, chicharrónes</p></li>
      <li class="menu-item"><h3>Beach Bum</h3><p>Maple fire roasted sweet potato, seasoned black beans, tropical slaw, toasted</p></li>
      <li class="menu-item"><h3>Island Time</h3><p>Battered avocado, sweet teriyaki glaze, charred pineapple, pickled red onion, queso fresco</p></li>
      <li class="menu-item"><h3>Tropical Shrimp</h3><p>Shrimp tempura, avocado smash, tropical slaw, sweet heat creama, toasted coconut</p></li>
      <li class="menu-item"><h3>Cabo Fish</h3><p>Beer battered cod, pickled cabbage, spicy escabeche and smoky homemade morita mayo</p></li>
    </ul>
  </div>

  <div class="panel panel--sky" style="left:16px;top:608px;width:420px;height:156px;">
    <div class="section-tab section-tab--bowl">Bowl Me Over!</div>
    <span class="bubble" style="left:366px;top:-2px;width:28px;height:28px;"></span>
    <span class="bubble" style="left:352px;top:30px;width:18px;height:18px;"></span>
    <p class="section-note section-note--bowl">Make any Breezy Burro taco into a bowl</p>
    <ul class="menu-list menu-list--bowls" style="left:44px;top:62px;gap:8px;">
      <li class="menu-item"><h3>Ensalada</h3><p>Chopped field greens, black beans, elote, avocado smash, fresh cilantro &amp; queso fresco</p></li>
      <li class="menu-item"><h3>Rice &amp; Beans</h3><p>Traditional Mexican arroz verde, seasoned black beans &amp; queso fresco</p></li>
    </ul>
  </div>
  <div class="illustration" role="img" aria-label="Sketch of two chicken drumsticks" style="left:326px;top:692px;width:96px;height:90px;"></div>

  <div class="panel panel--yellow" style="left:16px;top:784px;width:420px;height:144px;">
    <div class="section-tab section-tab--drink">Drink</div>
    <ul class="drink-list">
      <li>Tea- 20 oz...</li>
      <li>Soda fountain 20 oz...</li>
      <li>Bottle soda- see selection</li>
      <li><span class="col-a">Draft beer...16 oz...</span><span>Pitcher...</span></li>
      <li>Bottle beer import/domestic-see selection</li>
      <li><span class="col-a">FZ margarita 16 oz...</span><span>Pitcher...</span></li>
      <li><span class="col-a">Tap margarita 16 oz...</span><span>Pitcher...</span></li>
      <li><span class="col-a">Sangria- 16 oz...</span><span>Pitcher..._</span></li>
      <li><span class="col-a col-a--wide">Tequila single shot- cheap...</span><span class="col-b">Standard...</span><span>Premium...</span></li>
      <li><span class="col-a col-a--wide">Tequila double shot -cheap...</span><span class="col-b">Standard...</span><span>Premium...</span></li>
    </ul>
  </div>
  <div class="illustration" role="img" aria-label="Sketch of a soda cup with a straw" style="left:374px;top:842px;width:68px;height:102px;"></div>
</section>

</body>
</html>
```